Holvern Incorporated

Holvern is a business that provides consulting, and manages and supplies trades persons in the construction and heavy industries sector. We build, do maintenance, install machinery, and can manage projects or jobs. Would like or prefer more clean, classic designs. Blacks/greys, but open to almost anything.

Target Market(s)

Industrial/Construction/Manufacturing

Industry/Entity Type

Construction Company

Contact Information for Business Card

Clean, business name on the front, possibly have the details on the back, but open to any ideas.

Logo Text

We currently do not have a slogan, open to ideas

Font styles to use
Serif
Sans Serif

Colors

Designer to choose colors to be used in the design.

Requirements
Should not have
• the oval is not my logo, was just an idea. please don't send 20 designs with the oval

```html
<!DOCTYPE html>
<html lang="en">
<head>
<meta charset="UTF-8">
<title>Holvern Incorporated – Business Card</title>
<link href="https://fonts.googleapis.com/css2?family=Libre+Baskerville:wght@400;700&family=Poppins:wght@400;500&display=swap" rel="stylesheet">
<style>
  :root {
    --backdrop: #0b0b0c;
    --card: #242424;
    --card-deep: #1b1b1b;
    --accent: #cfd82c;
    --ink-light: #f4f4f4;
    --ink-muted: #9a9a9a;
    --shadow: rgba(0, 0, 0, 0.6);
  }
  * { margin: 0; padding: 0; box-sizing: border-box; }
  html, body {
    width: 1200px;
    height: 900px;
    overflow: hidden;
    background: var(--backdrop);
  }
  .stage {
    width: 1200px;
    height: 900px;
    display: flex;
    flex-direction: column;
    align-items: center;
    justify-content: center;
    gap: 44px;
  }
  .card {
    position: relative;
    width: 630px;
    height: 360px;
    background: var(--card);
    box-shadow: 0 18px 40px var(--shadow);
    overflow: hidden;
  }
  .card__edge {
    position: absolute;
    left: 0;
    right: 0;
    bottom: 0;
    height: 5px;
    background: var(--accent);
  }
  .brand-name {
    font-family: "Libre Baskerville", serif;
    font-weight: 400;
    letter-spacing: 0.04em;
    text-transform: uppercase;
  }
  /* Front */
  .card--front .brand-name {
    position: absolute;
    left: 0;
    right: 0;
    top: 120px;
    text-align: center;
    font-size: 54px;
    color: var(--card-deep);
    text-shadow: 0 1px 0 rgba(255, 255, 255, 0.06);
  }
  /* Back */
  .holder {
    position: absolute;
    left: 44px;
    top: 48px;
  }
  .holder__name {
    font-family: "Libre Baskerville", serif;
    font-weight: 700;
    font-size: 30px;
    color: var(--ink-light);
  }
  .holder__surname { color: var(--accent); }
  .holder__role {
    margin-top: 4px;
    font-family: "Poppins", sans-serif;
    font-size: 14px;
    color: var(--ink-muted);
  }
  .card--back .brand-name {
    position: absolute;
    right: 44px;
    top: 140px;
    font-size: 36px;
    color: var(--ink-light);
  }
  .contact {
    position: absolute;
    left: 44px;
    bottom: 46px;
    font-family: "Poppins", sans-serif;
    font-size: 13px;
    line-height: 1.55;
    color: var(--ink-light);
    list-style: none;
  }
  .contact__label { color: var(--accent); }
  .contact__address {
    margin-top: 12px;
    font-size: 15px;
    color: var(--accent);
  }
</style>
</head>
<body>
  <main class="stage">
    <section class="card card--front" aria-label="Card front">
      <p class="brand-name">Holvern</p>
      <span class="card__edge"></span>
    </section>

    <section class="card card--back" aria-label="Card back">
      <div class="holder">
        <p class="holder__name">Daniel <span class="holder__surname">Marlowe</span></p>
        <p class="holder__role">Co Founder of Holvern</p>
      </div>

      <p class="brand-name">Holvern</p>

      <ul class="contact">
        <li><span class="contact__label">Phone:</span> (1) 204 550 1937</li>
        <li><span class="contact__label">Mobile:</span> +44 7700 900 412</li>
        <li><span class="contact__label">Email:</span> info@holvern.com</li>
        <li><span class="contact__label">Web:</span> www.holvern.com</li>
        <li class="contact__address">58 Carden Row West, Ashford, TN4 2GH</li>
      </ul>
      <span class="card__edge"></span>
    </section>
  </main>
</body>
</html>
```